Brochure Design Project

A3 booklet folded in half to create an A4 booklet with front cover, inside two A4 pages and back cover. So four actual A4 pages in total to read! Logo should be attached.

This is a Business to Business brochure being given out to 1500 companies next Tuesday, Wednesday and Thursday, hence the rush to get the design so we can print it in time.

We are approaching businesses at a show called TerraFair and giving them a company brochure that presents to 10 steps for businesses to save resources, energy and money, whilst also becoming more sustainable. The companies we are approaching can actually win new clients by showing them that their business is responsible and sustainable.

In the link below the picture and statement "It is not just your business's future, but also your family's" is a powerful statement and I think could empower businesses to take action within the business, to help their families and future generations. I also like having smiley faces as it brightens up a brochure.

http://www.pixelbazaar.example/work/71254/leaflet-by-quillmark-studio

Similarly, I like the simplicity of the bottom of this page - the blue box makes it look corporate.

http://www.pixelbazaar.example/work/68391/letterhead-by-quillmark-studio

I've pasted some information about VerdaLink below which should go in the brochure:

VerdaLink helps businesses:

* Find environmental, ethical and sustainable products/services
* Cut through 'green-wash' or 'spin' to secure genuine providers
* Put contracts out to tender and negotiate the best overall deal amongst suppliers
* Secure a better deal than could be obtained individually as a business, because VerdaLink deal in volume
* Win new customers by showing other businesses that your business is sustainable
* Avoid the risks of non-compliance with environmental legislation
* Promote their green credentials both on and off-line through Directory listings, independent reviews and PR news feeds.

By working with VerdaLink, businesses gain new customers as well as saving resources, energy and money.

I am giving you all complete flexibility to come up with something good but I'm just letting you know some of the things I like although I'm no graphic designer but we do want to impress clients with the brochure. We'll then use the same type of design on our website to keep it consistent with our brochures and business cards (which I also really need doing for next week to so maybe you an help).

Regarding the 10 steps to making their business more sustainable, green and ethical, they are as follows and I've included some comments/testimonials for each step. You don't need to have the word testimonial written there if it looks repetitive. It could just be displayed as a comment. I suggest we have an istock photo to illustrate each of the 10 steps.

STEP 1 - SWITCH TO A GREEN ENERGY TARIFF

Did you know that 1/3 of all pollution comes from generating electricity from coal and gas? By sourcing your electricity from 100% wind, hydro or solar, as well as sourcing gas from landfill methane, you take the single biggest step in cutting emissions.

TESTIMONIAL:

"64 per cent of people polled in a recent survey would consider switching to a green energy tariff". NRT

STEP 2 - SWITCH TO GREEN WEBSITE HOSTING

Did you know that datacentres consume 1.5% of the world's total electricity production and cost £28.2bn a year to run? Switch to a hosting company that invests in the latest energy efficient servers and offsets their emissions.

TESTIMONIAL:

"Having a reliable hosting solution is essential to our continued success. I knew that we needed to outsource our hosting infrastructure if we were to remain on our current growth trajectory and keep improving our customer experience."
GORDON HALE, IT DIRECTOR, MARLOW'S BAGELS

STEP 3 - INSTALL LED/LOW ENERGY LIGHTING

Did you know that 80% of typical light bulb enerry is emitted as heat whereas newer bulbs are up to 90% more efficient emitting energy as light only. We help you identify energy efficient bulbs and identify relevant local grants or funding.

TESTIMONIAL:

"We've installed £10K worth of GU10 LED light bulbs and our monthly lighting bill dropped from £1700 to £400 due to the light bulbs only consuming 4W of energy each rather than 50W." BRAMBLEY HOTEL, ASHFORD

STEP 4 - GET LOW VOLTAGE OPTIMISATION

Did you know that business equipment needs 220V rather than 240V and excess voltage costs up to 20% more in energy costs and wears out electronic goods faster. With low-voltage optimisation the supply is smoothed and surge protected.

TESTIMONIAL:

"Two units have now been operating for over 6 months and, from careful analysis of electricity consumption, it is clear that an average reduction in usage of 9.1% has been achieved." JAN TORLOW, PWRAUTH

STEP 5 - CARBON OFFSET WITH TREES

Did you know that each person emits 9.5 tons of CO2 per year in the UK and 18 tons in the USA? The only efficient method of absorbing CO2 is to plant trees. Encourage employees to plant for £5-£15/month. Then match their effort.

TESTIMONIAL:

"Servnest has agreed to have a tree planted for every new customer, as a way to mitigate some of the carbon generated through its hosted servers." SERVNEST.

STEP 6 - INSTALL SOLAR/WIND GENERATION

Did you know that with the government Renewable Obligation (RO) and Renewable Heat Incentive (RHI) it is a good time to invest in solar PV or wind turbines. If you are a business, community project or church, we can advise how to do this.

TESTIMONIAL:

"This will allow many people to invest in small-scale low-carbon electricity, in return for a guaranteed payment from an electricity supplier of their choice for the electricity they generate and use as well as a guaranteed payment for unused surplus electricity they export back to the grid." MRHB

STEP 7 - GET ISO14001 ACCREDITATION

Did you know that receiving the ISO 14001 Environmental Accreditation and Certification Mark for your business will help you cut costs and even win new contracts. Show off the mark on corporate livery, email signatures and websites.

TESTIMONIAL:

"We first achieved ISO14001 accreditation in 2008. We will continue to fulfil the requirements of the standard." PETER HALVORSEN, CEO, GNT.

STEP 8 - GET GREEN PR/ONLINE MARKETING

Did you know that as part of your Marketing/PR strategy, VerdaLink promote many organisations in the sustainable sections of the press and at shows. We create unique content which is distributed via green directories, articles and blogs.

TESTIMONIAL:

"Since 2008 VerdaLink has helped Voltwise secure thousands of new customers through on-line and offline marketing strategies." MARK DENBY, SALES DIRECTOR, VOLTWISE.

STEP 9 - GET AN ECOLOGICAL/ECONOMICAL OFFICE

Did you know that you can rent a desk(s) at the HubDesk in Holborn, London or Brighton? The energy and stationary used is sustainably sourced. Similarly, if you have an empty office space, we can get you up to 50% off your rates bill.

TESTIMONIAL:

"We moved into a shared office in Central London which was heavily discounted. As a social enterprise, the landlord got a 50% reduction in his rates when we moved in. Before that, the space was empty for 2 years and he was still paying full rates."
SIMON PRESCOTT, FOUNDER, UK ALERT

STEP 10 - SWITCH TO ETHICAL SERVICES

Did you know that many companies believe that ethically sourced products and services are a key part of corporate CSR strategy? Select ethical banking and insurance products as well as sustainable hotels when on the move.

TESTIMONIAL:

"The business is mainly event-driven, so a quick response is really important. That boosts credibility, and it's something The Harbourline Bank is very good at." SYNDICATIONS, FALKIRK HOLLIS

CALL OUR TEAM AND WE WILL HELP YOUR BUSINESS IMPLEMENT THE STEPS RELEVANT TO YOUR ORGANISATION, USING THE RIGHT SUPPLIERS.

T: 0844 382 6270 quoting QRV7-2012 to get the normal charge for the switching service waived.

London Office:
Old Lantern Court
87 Mulberry Parade
London WC2X 9QT

Edinburgh Office:
61 Thistle Bank Road
Edinburgh EH7 2RZ

e: info@verdalink.example
t: +44 (0) 844 382 6270
f: +44 (0) 844 382 6271

Legal Name: VerdaLink Limited
Registered Company No: SC482735
Data Controller: z4127539
VAT Registration No: 853 4472 09

Target Market(s)

Environmental Businesses that want to use VerdaLink to switch to green and/or ethical products and services.

Industry/Entity Type

Graphic Designer

Requirements
Must have
• Be professional, corporate but inspiring. Pictures say a 1000 words. I like happy smiling people but not cheesy.
Nice to have
• Pictures for each of the 10 items. Just input the istock picture reference and size and I can pay for that separately. Not sure of the process with pictures on this site?

```html
<!DOCTYPE html>
<html lang="en">
<head>
<meta charset="utf-8">
<title>TerraFair – 10 Steps Spread</title>
<link rel="stylesheet" href="https://fonts.googleapis.com/css2?family=PT+Sans:wght@400;700&display=swap">
<style>
:root{
  --canvas:#ffffff;
  --page-left:#eeeeee;
  --page-right-a:#d9d9d9;
  --page-right-b:#efefef;
  --green:#5fb234;
  --green-light:#8fd14f;
  --panel-a:#1f6b93;
  --panel-b:#134a6e;
  --quote:#bcd7ea;
  --white:#ffffff;
  --grey-text:#8a8a8a;
}
*{box-sizing:border-box;margin:0;padding:0}
html,body{width:1200px;height:846px;overflow:hidden;background:var(--canvas)}
body{font-family:"PT Sans",Arial,sans-serif;position:relative}
.page{position:absolute;top:6px;height:834px}
.page-left{left:6px;width:592px;background:var(--page-left)}
.page-right{left:598px;width:596px;background:linear-gradient(90deg,var(--page-right-a),var(--page-right-b) 12%,var(--page-right-b))}
.step{position:absolute;width:534px;height:140px;box-shadow:3px 5px 7px rgba(0,0,0,.35)}
.page-left .step{left:29px}
.page-right .step{left:27px}
.step-visual{position:absolute;left:0;top:0;width:177px;height:140px}
.step-number{position:absolute;left:8px;top:6px;width:56px;height:42px;background:var(--green);color:var(--white);font-weight:700;font-size:30px;line-height:42px;text-align:center;border:2px solid rgba(255,255,255,.6)}
.step-title{position:absolute;left:106px;right:0;top:0;height:24px;background:linear-gradient(180deg,var(--green-light),var(--green));clip-path:polygon(14px 0,100% 0,100% 100%,0 100%);color:var(--white);font-weight:700;font-size:13.5px;line-height:24px;padding-left:40px;letter-spacing:.2px}
.step-body{position:absolute;left:177px;right:0;top:24px;bottom:0;background:linear-gradient(180deg,var(--panel-a),var(--panel-b));color:var(--white);padding:7px 10px 0 10px}
.step-body p{font-size:10.4px;line-height:12.6px;font-weight:700}
.step-body blockquote{margin-top:7px;font-size:9.4px;line-height:11.4px;color:var(--quote)}
.step-body blockquote.small{font-size:8px;line-height:9.8px}
.step-body blockquote.large{font-size:12px;line-height:14px;font-weight:700}
.step-body cite{font-style:normal;font-weight:700;text-transform:uppercase}
.visual-grass{background:linear-gradient(160deg,#dfe7e2 0%,#9ccf57 45%,#3f7f22 100%)}
.visual-hosting{background:linear-gradient(135deg,#ffffff 0%,#e3f0f5 50%,#7dc243 100%)}
.visual-led{background:radial-gradient(circle at 60% 50%,#e6f3ff 0%,#4a82c4 30%,#0e2a5a 100%)}
.visual-voltage{background:linear-gradient(160deg,#1a2b6a 0%,#5a86d6 50%,#12204a 100%)}
.visual-seedling{background:radial-gradient(circle at 50% 60%,#6b4a2c 0%,#c79a78 35%,#f7f2ec 70%,#ffffff 100%)}
.visual-solar{background:linear-gradient(180deg,#d3e6f3 0%,#9ec3de 45%,#3b5b7e 70%,#6ea23a 100%)}
.visual-iso{background:linear-gradient(90deg,#ffffff 70%,#d9d9d9);display:flex;align-items:center;justify-content:center;color:var(--green);font-weight:700;font-size:25px}
.visual-portrait{background:linear-gradient(160deg,#a9c27c 0%,#6f8f48 45%,#3a2c26 100%)}
.visual-placeholder{background:linear-gradient(90deg,#ffffff 70%,#d9d9d9);display:flex;align-items:center;justify-content:center;color:var(--grey-text);font-weight:700;font-size:22px}
</style>
</head>
<body>
<section class="page page-left">
  <article class="step" style="top:16px">
    <div class="step-visual visual-grass" role="img" aria-label="Photo of a white power socket with a plug in green grass"></div>
    <div class="step-number">01</div>
    <h2 class="step-title">SWITCH TO A GREEN ENERGY TARIFF</h2>
    <div class="step-body">
      <p>Did you know that 1/3 of all pollution comes from generating electricity from coal and gas? By sourcing your electricity from 100% wind, hydro or solar, as well as sourcing gas from landfill methane, you take the single biggest step in cutting emissions.</p>
      <blockquote style="margin-top:16px">"64 per cent of people polled in a recent survey would consider switching to a green energy tariff". &nbsp;&nbsp;&nbsp;&nbsp;&nbsp;- <cite>NRT</cite></blockquote>
    </div>
  </article>
  <article class="step" style="top:175px">
    <div class="step-visual visual-hosting" role="img" aria-label="Photo of a green network cable plug"></div>
    <div class="step-number">02</div>
    <h2 class="step-title">SWITCH TO GREEN WEBSITE HOSTING</h2>
    <div class="step-body">
      <p>Did you know that datacentres consume 1.5% of the world's total electricity production and cost £28.2bn a year to run? Switch to a hosting company that invests in the latest energy efficient servers and offsets their emissions.</p>
      <blockquote>"Having a reliable hosting solution is essential to our continued success. I knew that we needed to outsource our hosting infrastructure if we were to remain on our current growth trajectory and keep improving our customer experience."<br><cite>GORDON HALE, IT DIRECTOR, MARLOW'S BAGELS</cite></blockquote>
    </div>
  </article>
  <article class="step" style="top:329px">
    <div class="step-visual visual-led" role="img" aria-label="Photo of a glowing LED light bulb on a blue background"></div>
    <div class="step-number">03</div>
    <h2 class="step-title">INSTALL LED/LOW ENERGY LIGHTING</h2>
    <div class="step-body">
      <p>Did you know that 80% of typical light bulb enerry is emitted as heat whereas newer bulbs are up to 90% more efficient emitting energy as light only. We help you identify energy efficient bulbs and identify relevant local grants or funding.</p>
      <blockquote>"We've installed £10K worth of GU10 LED light bulbs and our monthly lighting bill dropped from £1700 to £400 due to the light bulbs only consuming 4W of energy each rather than 50W." <cite>BRAMBLEY HOTEL, ASHFORD</cite></blockquote>
    </div>
  </article>
  <article class="step" style="top:488px">
    <div class="step-visual visual-voltage" role="img" aria-label="Photo of a row of blue LED components"></div>
    <div class="step-number">04</div>
    <h2 class="step-title">GET LOW VOLTAGE OPTIMISATION</h2>
    <div class="step-body">
      <p>Did you know that datacentres consume 1.5% of the world's total electricity production and cost £28.2bn a year to run? Switch to a hosting company that invests in the latest energy efficient servers and offsets their emissions.</p>
      <blockquote>"Having a reliable hosting solution is essential to our continued success. I knew that we needed to outsource our hosting infrastructure if we were to remain on our current growth trajectory and keep improving our customer experience."<br><cite>GORDON HALE, IT DIRECTOR, MARLOW'S BAGELS</cite></blockquote>
    </div>
  </article>
  <article class="step" style="top:642px">
    <div class="step-visual visual-seedling" role="img" aria-label="Photo of cupped hands holding soil with a young seedling"></div>
    <div class="step-number">05</div>
    <h2 class="step-title">CARBON OFFSET WITH TREES</h2>
    <div class="step-body">
      <p>Did you know that each person emits 9.5 tons of CO2 per year in the UK and 18 tons in the USA? The only efficient method of absorbing CO2 is to plant trees. Encourage employees to plant for £5-£15/month. Then match their effort.</p>
      <blockquote>"Servnest has agreed to have a tree planted for every new customer, as a way to mitigate some of the carbon generated through its hosted servers." <cite>SERVNEST.</cite></blockquote>
    </div>
  </article>
</section>

<section class="page page-right">
  <article class="step" style="top:16px">
    <div class="step-visual visual-solar" role="img" aria-label="Photo of solar panels and wind turbines under a blue sky"></div>
    <div class="step-number">06</div>
    <h2 class="step-title">INSTALL SOLAR/WIND GENERATION</h2>
    <div class="step-body">
      <p>Did you know that with the government Renewable Obligation (RO) and Renewable Heat Incentive (RHI) it is a good time to invest in solar PV or wind turbines. If you are a business, community project or church, we can advise how to do this.</p>
      <blockquote class="small">"This will allow many people to invest in small-scale low-carbon electricity, in return for a guaranteed payment from an electricity supplier of their choice for the electricity they generate and use as well as a guaranteed payment for unused surplus electricity they export back to the grid." <cite>MRHB</cite></blockquote>
    </div>
  </article>
  <article class="step" style="top:175px">
    <div class="step-visual visual-iso">ISO 14001</div>
    <div class="step-number">07</div>
    <h2 class="step-title">GET ISO14001 ACCREDITATION</h2>
    <div class="step-body">
      <p>Did you know that receiving the ISO 14001 Environmental Accreditation and Certification Mark for your business will help you cut costs and even win new contracts. Show off the mark on corporate livery, email signatures and websites.</p>
      <blockquote class="large">"We first achieved ISO14001 accreditation in 2008. We will continue to fulfil the requirements of the standard." <cite>PETER HALVORSEN, CEO, GNT.</cite></blockquote>
    </div>
  </article>
  <article class="step" style="top:329px">
    <div class="step-visual visual-portrait" role="img" aria-label="Photo of a smiling businesswoman in a dark jacket outdoors"></div>
    <div class="step-number">08</div>
    <h2 class="step-title">GET GREEN PR/ONLINE MARKETING</h2>
    <div class="step-body">
      <p>Did you know that as part of your Marketing/PR strategy, VerdaLink promote many organisations in the sustainable sections of the press and at shows. We create unique content which is distributed via green directories, articles and blogs.</p>
      <blockquote>"Since 2008 VerdaLink has helped Voltwise secure thousands of new customers through on-line and offline marketing strategies." <cite>MARK DENBY, SALES DIRECTOR, VOLTWISE.</cite></blockquote>
    </div>
  </article>
  <article class="step" style="top:488px">
    <div class="step-visual visual-placeholder">PHOTO</div>
    <div class="step-number">09</div>
    <h2 class="step-title">GET AN ECOLOGICAL/ECONOMICAL OFFICE</h2>
    <div class="step-body">
      <p>Did you know that you can rent a desk(s) at the HubDesk in Holborn, London or Brighton? The energy and stationary used is sustainably sourced. Similarly, if you have an empty office space, we can get you up to 50% off your rates bill.</p>
      <blockquote class="small" style="margin-top:3px">"We moved into a shared office in Central London which was heavily discounted. As a social enterprise, the landlord got a 50% reduction in his rates when we moved in. Before that, the space was empty for 2 years and he was still paying full rates."<br><cite>SIMON PRESCOTT, FOUNDER, UK ALERT</cite></blockquote>
    </div>
  </article>
  <article class="step" style="top:642px">
    <div class="step-visual visual-seedling" role="img" aria-label="Photo of cupped hands holding soil with a young seedling"></div>
    <div class="step-number">10</div>
    <h2 class="step-title">SWITCH TO ETHICAL SERVICES</h2>
    <div class="step-body">
      <p>Did you know that many companies believe that ethically sourced products and services are a key part of corporate CSR strategy? Select ethical banking and insurance products as well as sustainable hotels when on the move.</p>
      <blockquote>"The business is mainly event-driven, so a quick response is really important. That boosts credibility, and it's something The Harbourline Bank is very good at." <cite>SYNDICATIONS, FALKIRK HOLLIS</cite></blockquote>
    </div>
  </article>
</section>
</body>
</html>
```